Australian Meat, Seafood and Fresh Produce Website

Our organization is looking to design a simple, but eye catching website to show our services.
Our company exports West Australian FRESH fruit and vegetables, seafood and meat.
The website we are looking for would consist of:
- Landing Page
- Company info
- Directors bio
- Page that highlights our products
- Contact us page
We would like it to have a Chinese translated version as well.
Tobin
Target Market(s)
Chinese Market
Industry/Entity Type
It Company
Number of Pages Required
1 page
Look and feel
Each slider illustrates characteristics of the customer's brand and the style your logo design should communicate.

```html
<!DOCTYPE html>
<html lang="en">
<head>
<meta charset="utf-8">
<title>Fresh Produce Export</title>
<link href="https://fonts.googleapis.com/css2?family=Open+Sans:wght@400;600;700&display=swap" rel="stylesheet">
<style>
:root{
  --orange:#f7802d;
  --green:#7fbf3f;
  --green-dark:#4d6e27;
  --band-green:#6aa534;
  --text-grey:#5a5a5a;
  --rule:#9a9a9a;
  --hero-bg:#efefef;
  --title-brown:#8a3a1a;
  --white:#ffffff;
}
*{margin:0;padding:0;box-sizing:border-box}
html,body{width:1200px;height:1076px;overflow:hidden;background:var(--white);font-family:'Open Sans',sans-serif}
.page{position:relative;width:1200px;height:1076px}
.hero{position:absolute;left:0;top:0;width:1200px;height:317px;background:var(--hero-bg)}
.hero-photo{position:absolute;left:0;top:0;width:560px;height:317px;
  background:radial-gradient(ellipse at 20% 40%,#e8a070 0%,#c9c0a8 35%,#e5e3de 65%,var(--hero-bg) 100%)}
.step-circle{position:absolute;width:64px;height:64px;border:2px solid var(--green);border-radius:50%;
  color:var(--green);font-size:42px;line-height:58px;text-align:center;font-weight:400}
.step-arrow{position:absolute;top:87px}
.step-icon{position:absolute;top:166px}
.step-label{position:absolute;top:236px;width:120px;text-align:center;font-size:21px;color:#222;font-weight:400}
.service{position:absolute;top:380px;width:240px;text-align:center}
.service-photo{width:240px;height:165px;border:7px solid var(--orange)}
.service-title{margin:18px auto 0;width:212px;padding-bottom:4px;border-bottom:1px solid var(--rule);
  color:var(--green);font-size:21px;font-weight:400;letter-spacing:.3px}
.service-text{margin-top:13px;font-size:13.3px;line-height:21.5px;color:var(--text-grey)}
.read-more{display:inline-block;margin-top:18px;width:100px;height:30px;line-height:30px;background:var(--orange);
  color:var(--white);font-size:12.5px;text-decoration:none}
.testimonial{position:absolute;left:0;top:772px;width:1200px;height:304px;
  background:linear-gradient(90deg,var(--band-green) 0%,#74ad3a 70%,#8a9a4c 78%,#a06a45 100%)}
.testimonial-photo{position:absolute;right:0;top:0;width:300px;height:304px;
  background:radial-gradient(circle at 40% 30%,#d63a2a 0%,#c85040 30%,#b58a6a 60%,rgba(160,110,70,0) 100%)}
.testimonial-title{position:absolute;left:82px;top:44px;font-size:27px;color:var(--title-brown);font-weight:400}
.testimonial-nav{position:absolute;left:267px;top:52px}
.testimonial-rule{position:absolute;left:80px;top:89px;width:773px;height:1px;background:#7a3a1a}
.quote-mark{position:absolute;font-size:110px;line-height:1;color:var(--green-dark);font-weight:700;font-family:Georgia,serif}
.quote-text{position:absolute;left:132px;top:115px;width:730px;font-size:13.3px;line-height:21.5px;color:var(--white)}
.author-name{position:absolute;left:133px;top:224px;font-size:14px;font-weight:600;color:#1e2a10}
.author-role{position:absolute;left:146px;top:243px;font-size:11px;color:#1e2a10}
</style>
</head>
<body>
<div class="page">
  <section class="hero">
    <div class="hero-photo" role="img" aria-label="Fresh fish, prawns, herbs, bay leaves and peppercorns"></div>

    <div class="step-circle" style="left:614px;top:63px">1</div>
    <div class="step-circle" style="left:835px;top:63px">2</div>
    <div class="step-circle" style="left:1055px;top:63px">3</div>

    <svg class="step-arrow" style="left:690px" width="132" height="16" viewBox="0 0 132 16">
      <g fill="#f7802d"><circle cx="4" cy="8" r="2.5"/><circle cx="19" cy="8" r="2.5"/><circle cx="34" cy="8" r="2.5"/><circle cx="49" cy="8" r="2.5"/><circle cx="64" cy="8" r="2.5"/><circle cx="79" cy="8" r="2.5"/><circle cx="94" cy="8" r="2.5"/><circle cx="109" cy="8" r="2.5"/><path d="M116 0 L130 8 L116 16 L121 8Z"/></g>
    </svg>
    <svg class="step-arrow" style="left:911px" width="132" height="16" viewBox="0 0 132 16">
      <g fill="#f7802d"><circle cx="4" cy="8" r="2.5"/><circle cx="19" cy="8" r="2.5"/><circle cx="34" cy="8" r="2.5"/><circle cx="49" cy="8" r="2.5"/><circle cx="64" cy="8" r="2.5"/><circle cx="79" cy="8" r="2.5"/><circle cx="94" cy="8" r="2.5"/><circle cx="109" cy="8" r="2.5"/><path d="M116 0 L130 8 L116 16 L121 8Z"/></g>
    </svg>

    <svg class="step-icon" style="left:600px" width="94" height="60" viewBox="0 0 94 60">
      <g fill="#4d6e27">
        <rect x="26" y="2" width="12" height="8"/>
        <path d="M24 10h16v8c6 4 8 10 8 18v22H16V36c0-8 2-14 8-18z"/>
        <path d="M6 26c6-4 14 0 14 8v24H6C0 52 0 32 6 26z"/>
        <path d="M42 24c8-6 18-4 22 4 4 10 0 26-12 30-10 2-16-6-16-18 0-6 2-12 6-16z"/>
        <path d="M52 20c2-6 6-8 10-8-2 4-4 6-10 8z"/>
        <path d="M68 18c4 0 6 4 6 10 6 4 10 10 8 20-2 8-10 10-16 8-4-2-6-10-4-18 2-8 2-14 6-20z"/>
      </g>
    </svg>
    <svg class="step-icon" style="left:828px" width="72" height="62" viewBox="0 0 72 62">
      <g fill="none" stroke="#4d6e27" stroke-width="6" stroke-linejoin="round">
        <path d="M2 4h10l8 38h40"/>
        <path d="M14 12h54l-6 22H18"/>
      </g>
      <g fill="#4d6e27"><circle cx="24" cy="53" r="7"/><circle cx="54" cy="53" r="7"/></g>
      <g fill="#efefef"><circle cx="24" cy="53" r="3"/><circle cx="54" cy="53" r="3"/></g>
      <g stroke="#4d6e27" stroke-width="3"><line x1="18" y1="23" x2="64" y2="23"/></g>
    </svg>
    <svg class="step-icon" style="left:1034px" width="88" height="60" viewBox="0 0 88 60">
      <g fill="#4d6e27">
        <rect x="2" y="2" width="52" height="40" rx="3"/>
        <path d="M58 12h16l12 14v16H58z"/>
        <circle cx="20" cy="48" r="10"/><circle cx="68" cy="48" r="10"/>
      </g>
      <path d="M63 16h9l8 10H63z" fill="#efefef"/>
      <g fill="#efefef"><circle cx="20" cy="48" r="5"/><circle cx="68" cy="48" r="5"/></g>
    </svg>

    <div class="step-label" style="left:587px">BROWSE</div>
    <div class="step-label" style="left:804px">ORDER</div>
    <div class="step-label" style="left:1018px">ENJOY</div>
  </section>

  <section class="service" style="left:80px">
    <div class="service-photo" role="img" aria-label="Shopper choosing fresh vegetables at market" style="background:linear-gradient(90deg,#a08a80,#5f9a3e 60%,#c8493a)"></div>
    <h3 class="service-title">WHOLESALE</h3>
    <p class="service-text">It is a long established fact that a reader will be distracted by the readable content of a page when looking at its layout.</p>
    <a class="read-more" href="#">READ MORE</a>
  </section>
  <section class="service" style="left:347px">
    <div class="service-photo" role="img" aria-label="Chef plating dishes in a kitchen" style="background:linear-gradient(135deg,#e8e4df,#c9c2b8 50%,#b8a890)"></div>
    <h3 class="service-title">FOOD SERVICE</h3>
    <p class="service-text">It is a long established fact that a reader will be distracted by the readable content of a page when looking at its layout.</p>
    <a class="read-more" href="#">READ MORE</a>
  </section>
  <section class="service" style="left:614px">
    <div class="service-photo" role="img" aria-label="Family shopping for produce in a supermarket" style="background:linear-gradient(90deg,#d8a040,#b84a3a 50%,#7a8aa0)"></div>
    <h3 class="service-title">RETAIL</h3>
    <p class="service-text">It is a long established fact that a reader will be distracted by the readable content of a page when looking at its layout.</p>
    <a class="read-more" href="#">READ MORE</a>
  </section>
  <section class="service" style="left:881px">
    <div class="service-photo" role="img" aria-label="Supermarket produce aisle" style="background:linear-gradient(180deg,#3a3a3a,#8a7a5a 45%,#9aa4aa)"></div>
    <h3 class="service-title">EXPORT</h3>
    <p class="service-text">It is a long established fact that a reader will be distracted by the readable content of a page when looking at its layout.</p>
    <a class="read-more" href="#">READ MORE</a>
  </section>

  <section class="testimonial">
    <div class="testimonial-photo" role="img" aria-label="Tomatoes, mushrooms, herbs and raw meat on a wooden board"></div>
    <h2 class="testimonial-title">TESTIMONIAL</h2>
    <svg class="testimonial-nav" width="46" height="24" viewBox="0 0 46 24">
      <g fill="none" stroke="#4d6e27" stroke-width="2"><path d="M12 2 L2 12 L12 22"/><path d="M34 2 L44 12 L34 22"/></g>
    </svg>
    <div class="testimonial-rule"></div>
    <div class="quote-mark" style="left:78px;top:100px">“</div>
    <div class="quote-mark" style="left:474px;top:170px">”</div>
    <p class="quote-text">It is a long established fact that a reader will be distracted by the readable content of a page when looking at its layout. The point of using Lorem Ipsum is that it has a more-or-less normal distribution of letters, as opposed to &nbsp;here', making it look like readable English. Many desktop publishing packages and web page editors.Lorem Ipsum is that it has a more-or-less normal distribution of letters, as opposed.</p>
    <div class="author-name">Jared Tobin</div>
    <div class="author-role">Customer</div>
  </section>
</div>
</body>
</html>
```